Velvet Morn - 5 different skin care lotion bottles label designs

Packaging size labels see download files.
Every bottle has a front and a back label. They will be glued on the bottles.
Brand name is Velvet Morn. See uploaded logo. It's our private label.
We would like to have a uniform as possible appearance of the products (CI).
Please use background graphics.
Only Adobe Illustrator files.

Here are the download files (sizes, etc and more details):
www.lunaprint.de/2014/BriefHive/5labels.zip

To all, I've uploaded PDF files for 4 bottles. One bottle is already Illustrator, like we want to get the label design. Heike

Reason: We think the time window was to short.

```html
<!DOCTYPE html>
<html lang="en">
<head>
<meta charset="UTF-8">
<title>Velvet Morn – Skin Care Lotion Honey Almond Label</title>
<link rel="stylesheet" href="https://fonts.googleapis.com/css2?family=Source+Sans+3:wght@400;600;700&family=Jost:wght@400;600&display=swap">
<style>
  :root {
    --canvas-bg: #efefef;
    --label-top: #a6daf5;
    --label-mid: #7fcbf0;
    --label-low: #a3d9f4;
    --navy: #1b4a8a;
    --navy-deep: #16407c;
    --band: #1f5fa6;
    --band-text: #ffffff;
    --honey: #f0b447;
    --almond: #b8743d;
  }
  * { margin: 0; padding: 0; box-sizing: border-box; }
  html, body { width: 1035px; height: 1200px; overflow: hidden; background: var(--canvas-bg); }
  .canvas { position: relative; width: 1035px; height: 1200px; }

  .label {
    position: absolute; left: 297px; top: 130px; width: 440px; height: 940px;
    border-radius: 10px; overflow: hidden;
    background: linear-gradient(180deg, var(--label-top) 0%, var(--label-mid) 50%, var(--label-low) 100%);
    color: var(--navy);
    font-family: "Source Sans 3", sans-serif;
    text-align: center;
  }

  .brand {
    position: absolute; top: 80px; left: 0; right: 0;
    display: flex; align-items: center; justify-content: center; gap: 12px;
  }
  .brand__dot { width: 18px; height: 18px; border-radius: 50%; background: var(--navy); }
  .brand__name { font-size: 40px; font-weight: 600; line-height: 1; color: var(--navy); }

  .product-type { position: absolute; top: 200px; left: 0; right: 0; font-size: 45px; font-weight: 400; line-height: 1; }
  .product-name { position: absolute; top: 252px; left: 0; right: 0; font-size: 52px; font-weight: 700; line-height: 1; color: var(--navy-deep); }
  .product-claim { position: absolute; top: 308px; left: 0; right: 0; font-size: 32px; font-weight: 400; line-height: 1; letter-spacing: 1px; }
  .product-warning { position: absolute; top: 350px; left: 0; right: 0; font-size: 24px; font-weight: 700; line-height: 1; }

  .product-visual {
    position: absolute; top: 440px; left: 30px; width: 380px; height: 200px;
    border-radius: 24px;
    background: linear-gradient(160deg, var(--honey) 0%, var(--almond) 100%);
  }

  .product-copy {
    position: absolute; top: 700px; left: 26px; right: 26px;
    font-family: "Jost", sans-serif; font-size: 19.5px; line-height: 1.2;
    text-align: justify; text-align-last: center;
    color: var(--navy-deep);
  }
  .product-copy strong { display: block; font-weight: 600; text-align: center; }

  .volume-band {
    position: absolute; left: 0; right: 0; top: 880px; height: 56px;
    background: var(--band); color: var(--band-text);
    display: flex; align-items: center; justify-content: center;
    font-size: 34px; font-weight: 700;
  }
</style>
</head>
<body>
<div class="canvas">
  <section class="label">
    <div class="brand">
      <span class="brand__dot"></span>
      <span class="brand__name">Velvet Morn</span>
    </div>

    <h2 class="product-type">SKIN CARE LOTION</h2>
    <h1 class="product-name">HONEY ALMOND</h1>
    <p class="product-claim">Moisturizes and Smooths</p>
    <p class="product-warning">For external use only.</p>

    <div class="product-visual" role="img" aria-label="Photo of almonds with honey drizzling over them"></div>

    <p class="product-copy">
      Honey Almond Skin Care Lotion moisturizes and hydrates skin in an instant. This unique formula helps to restore skin`s natural smoothness. It is an excellent after-sun moisturizer.
      <strong>Absorbs quickly with no greasy feeling.</strong>
    </p>

    <div class="volume-band">591 ml /20 fl Oz</div>
  </section>
</div>
</body>
</html>
```